Pivots & Treads .com

This website is simple!!!
Landing page background image should capture the customers attention!!! We will provide a image as a example of what we like. The purpose for this website is to provide customers with a clean easy way to request a quote for industrial casters and wheels by OEM’s as well as maintenance departments worldwide. Please see if you can follow our thought process below.
Customer comes to website, they are invited to Request a Quote by providing us with Manufacturer Name, Manufacturers Part # and quantity needed.
If this is not known the customer will complete will WP conversation format form answering about 10 questions
Or
Look up the part number in one of the 8 to 12 catalogs located in the Flippin Book format on our catalog page, or equal plug in .
When the client request a quote a account page will pop up request The following:
Clients first and last name
Email address
And optional questions
Company name and best contact number.
Once this is complete customer will hit SUBMIT.
The customers request will be in system. A email will be sent to Customer service notifying us the Quote Request has been made.
We will then build a quote for the customer with a good, better and best options. Customers Request a Quote submission may have more than one caster or wheel requested at a time, so website must allow this.
When the customer comes back into website there email address will come up as the account name and request a password be made for them. This will allow them to store quotes in their account for future needs. If quote is older than 30 day the system will trigger a button at the bottom of the quote for resubmit Request for updated quote.
Once customer reviews quote the quote can be Converted to order within the website.
Once Converted the system will send us a email and order will be processed.
We will need a Chat program that will text to CS the questions.
You will need to have high quality graphic design skills on your team.
We have found 2 plugins that would work nicely with our new website Flippin books to showcase our catalogs for customers to research and WPForms conversation forms to complete request for quote form.
Just Ideas:
Very very ghosted caster blueprint in white background but very very ghosted or the icon just idea
We have never had a font used we like
Grayscale every except for rubber on wheels and logo icon
Website should have hamburger menu on left
Website should hav responsive deign
Account head on right side
Has anyone read the brief from top to bottom and the updates, I’m seeing a lot of duplicates of the website I posted in images I want a clean website With lite backgrand with the poly being definite colors on each wheel I added a green yellow and red image has anyone looked at that Just a question?
Went on vacation/holiday

```html
<!DOCTYPE html>
<html lang="en">
<head>
<meta charset="utf-8">
<title>Pivots &amp; Treads .com</title>
<link rel="stylesheet" href="https://fonts.googleapis.com/css2?family=Montserrat:wght@400;800&family=Raleway:wght@400;500&display=swap">
<style>
  :root {
    --brand-blue: #2f4690;
    --ink-black: #000000;
    --paper: #f7f7f7;
    --paper-edge: #ececec;
    --white: #ffffff;
    --step-ring: #c9d0e6;
    --wheel-navy: rgba(44, 59, 102, 0.30);
    --wheel-steel: rgba(170, 174, 182, 0.22);
    --wheel-iron: rgba(42, 39, 37, 0.26);
  }
  * { margin: 0; padding: 0; box-sizing: border-box; }
  html, body { width: 1200px; height: 585px; overflow: hidden; }
  body {
    position: relative;
    font-family: "Raleway", sans-serif;
    color: var(--white);
    background: radial-gradient(circle at 75% 40%, var(--white) 0%, var(--paper) 55%, var(--paper-edge) 100%);
  }
  a { text-decoration: none; color: inherit; }
  .hero-panel {
    position: absolute; left: 0; top: 0;
    width: 1200px; height: 529px;
  }
  .product-photo {
    position: absolute; left: 560px; top: 130px; width: 480px; height: 250px;
    background:
      radial-gradient(ellipse 30% 45% at 22% 55%, var(--wheel-navy) 0%, transparent 100%),
      radial-gradient(ellipse 30% 55% at 52% 50%, var(--wheel-steel) 0%, transparent 100%),
      radial-gradient(ellipse 26% 45% at 82% 55%, var(--wheel-iron) 0%, transparent 100%);
  }
  .brand {
    position: absolute; left: 164px; top: 30px;
    width: 246px; text-align: center;
  }
  .brand-mark {
    display: block; margin: 0 auto 14px;
    width: 40px; height: 40px; border-radius: 50%;
    border: 3px solid var(--white);
  }
  .brand-name {
    font-family: "Montserrat", sans-serif; font-weight: 800;
    font-size: 19px; letter-spacing: 0.5px; white-space: nowrap;
  }
  .headline {
    position: absolute; left: 163px; top: 164px;
    font-family: "Montserrat", sans-serif; font-weight: 800;
    font-size: 21px; line-height: 26px; letter-spacing: 0.2px;
  }
  .steps-title {
    position: absolute; left: 163px; top: 238px;
    font-family: "Montserrat", sans-serif; font-weight: 400; font-size: 22px;
    width: 267px; padding-bottom: 8px;
    border-bottom: 1px dashed var(--white);
  }
  .steps { position: absolute; left: 163px; top: 290px; list-style: none; }
  .step {
    position: relative; display: flex; align-items: center;
    height: 27px; margin-bottom: 13.5px;
    font-size: 19px; font-weight: 500;
  }
  .step-num {
    width: 26px; height: 26px; margin-right: 12px; border-radius: 50%;
    border: 3px solid var(--step-ring);
    display: flex; align-items: center; justify-content: center;
    font-size: 15px; font-family: "Montserrat", sans-serif;
  }
  .step + .step::before {
    content: ""; position: absolute; left: 12.5px; top: -14px;
    width: 1px; height: 14px; background: var(--step-ring);
  }
  .actions { position: absolute; left: 161px; top: 427px; display: flex; gap: 14px; }
  .btn {
    height: 37px; border-radius: 19px; display: flex; align-items: center; justify-content: center;
    font-family: "Montserrat", sans-serif; font-size: 13.5px; font-weight: 400; letter-spacing: 0.3px;
    color: var(--white);
  }
  .btn-outline { width: 169px; border: 1px solid var(--white); }
  .btn-solid { width: 113px; background: var(--ink-black); }
  .account {
    position: absolute; left: 859px; top: 20px; width: 131px; height: 37px;
    border-radius: 19px; background: var(--brand-blue);
    display: flex; align-items: center; padding-left: 4px;
    font-family: "Montserrat", sans-serif; font-size: 13.5px; color: var(--white);
  }
  .account-icon {
    width: 29px; height: 29px; border-radius: 50%; background: var(--white);
    display: flex; align-items: center; justify-content: center; margin-right: 11px;
  }
  .menu-toggle {
    position: absolute; left: 1001px; top: 19px; width: 38px; height: 38px;
    border-radius: 50%; border: 1px solid var(--brand-blue);
    display: flex; align-items: center; justify-content: center;
  }
  .site-footer {
    position: absolute; left: 0; top: 529px; width: 1200px; height: 56px;
    background: var(--ink-black);
    display: flex; align-items: center; justify-content: space-between;
    padding: 0 161px;
    font-family: "Raleway", sans-serif; font-size: 13.5px; letter-spacing: 0.3px;
  }
  .social { display: flex; gap: 6px; list-style: none; }
  .social li {
    width: 26px; height: 26px; border-radius: 50%; border: 1px solid var(--white);
  }
</style>
</head>
<body>
  <svg class="hero-panel" viewBox="0 0 1200 529" aria-hidden="true">
    <polygon points="0,0 416,0 741,529 0,529" fill="var(--brand-blue)"/>
  </svg>

  <div class="product-photo" role="img" aria-label="Photo of three industrial wheels: a blue polyurethane wheel, a swivel caster with steel plate, and a black cast iron wheel"></div>

  <header class="brand">
    <span class="brand-mark" aria-hidden="true"></span>
    <div class="brand-name">PIVOTS &amp; TREADS.com</div>
  </header>

  <h1 class="headline">#1 SOLUTION FOR<br>ALL YOUR APPLICATIONS.</h1>

  <h2 class="steps-title">Easy as 1-2-3</h2>
  <ol class="steps">
    <li class="step"><span class="step-num">1</span>Request Quote</li>
    <li class="step"><span class="step-num">2</span>Receive a Quote</li>
    <li class="step"><span class="step-num">3</span>Convert a Quote to Order.</li>
  </ol>

  <nav class="actions">
    <a class="btn btn-outline" href="#">REQUEST QUOTE</a>
    <a class="btn btn-solid" href="#">CATALOG</a>
  </nav>

  <a class="account" href="#">
    <span class="account-icon">
      <svg width="16" height="16" viewBox="0 0 16 16" fill="none" stroke="var(--brand-blue)" stroke-width="1.6" stroke-linecap="round">
        <circle cx="7" cy="5" r="3"/>
        <path d="M2 14c0-3 2.2-5 5-5"/>
        <path d="M12 9v5M9.5 11.5h5"/>
      </svg>
    </span>ACCOUNT
  </a>
  <a class="menu-toggle" href="#" aria-label="Menu">
    <svg width="18" height="14" viewBox="0 0 18 14" stroke="var(--brand-blue)" stroke-width="2.4" stroke-linecap="round">
      <path d="M2 2h14M2 7h14M2 12h14"/>
    </svg>
  </a>

  <footer class="site-footer">
    <p>Copyright © 2022 PIVOTS &amp; TREADS.com. All Rights Reserved.</p>
    <ul class="social" aria-label="Social links">
      <li aria-label="Social link 1"></li>
      <li aria-label="Social link 2"></li>
      <li aria-label="Social link 3"></li>
      <li aria-label="Social link 4"></li>
    </ul>
  </footer>
</body>
</html>
```